Business card for law firm

Need business card for new law firm. Think confident, authoritative, conservative, but not stuffy or old-fashioned.

Contact Information for Business Card

Content for card - logo (uploaded), plus the following:

Paul Weybridge (larger font)
Managing Partner (larger font, but not as large as name)
Level 9, 47 Calder Lane
Sydney NSW 2000
Main Tel 02 7304 6219
Direct Tel 02 7462 3158
Email paul@wbrlegal.com.au
www.wbrlegal.com.au

Letterhead design should include logo plus:
Level 9, 47 Calder Lane
Sydney NSW 2000
Tel 02 7462 3158
www.wbrlegal.com.au

```html
<!DOCTYPE html>
<html lang="en">
<head>
<meta charset="utf-8">
<title>Weybridge Lawyers – Business Card</title>
<link rel="stylesheet" href="https://fonts.googleapis.com/css2?family=Cinzel:wght@500;600&family=Montserrat:wght@400;500&display=swap">
<style>
  :root {
    --stage: #161616;
    --card: #232323;
    --card-light: #2b2b2b;
    --ink: #f4f4f4;
    --ink-soft: #dcdcdc;
    --edge: #27307a;
  }
  * { box-sizing: border-box; margin: 0; padding: 0; }
  html, body { width: 1200px; height: 900px; overflow: hidden; background: var(--stage); }
  .stage {
    width: 1200px; height: 900px;
    display: flex; flex-direction: column; align-items: center; justify-content: center;
    gap: 44px;
  }
  .card {
    position: relative;
    width: 700px; height: 400px;
    background: linear-gradient(135deg, var(--card) 0%, var(--card-light) 70%, var(--card) 100%);
    border-bottom: 5px solid var(--edge);
    box-shadow: 0 18px 40px rgba(0,0,0,0.55);
    color: var(--ink);
  }
  .brand {
    display: flex; align-items: center; gap: 14px;
    font-family: "Cinzel", serif; font-weight: 500;
    color: var(--ink);
    letter-spacing: 0.04em;
  }
  .brand-mark { width: 16px; height: 16px; background: var(--ink); flex: none; }
  .card--front { display: flex; align-items: center; justify-content: center; }
  .card--front .brand { font-size: 40px; }
  .card--back { display: flex; align-items: center; }
  .card--back .brand-block { width: 360px; display: flex; justify-content: center; }
  .card--back .brand { font-size: 27px; }
  .divider { width: 1.5px; height: 250px; background: var(--ink-soft); }
  .contact { padding-left: 40px; font-family: "Montserrat", sans-serif; }
  .contact-name {
    font-family: "Cinzel", serif; font-weight: 600;
    font-size: 27px; letter-spacing: 0.02em; line-height: 1.1;
  }
  .contact-role { font-size: 17px; color: var(--ink-soft); margin-bottom: 14px; }
  .contact-address { font-size: 17px; line-height: 1.35; margin-bottom: 14px; font-style: normal; }
  .contact-list { list-style: none; font-size: 17px; line-height: 1.55; }
  .contact-list li { display: flex; align-items: center; gap: 14px; }
  .icon { width: 14px; height: 14px; flex: none; stroke: var(--ink); fill: none; stroke-width: 1.6; }
</style>
</head>
<body>
<main class="stage">
  <section class="card card--front" aria-label="Card front">
    <div class="brand"><span class="brand-mark"></span>Weybridge Lawyers</div>
  </section>

  <section class="card card--back" aria-label="Card back">
    <div class="brand-block">
      <div class="brand"><span class="brand-mark"></span>Weybridge Lawyers</div>
    </div>
    <div class="divider"></div>
    <div class="contact">
      <h1 class="contact-name">Paul Weybridge</h1>
      <p class="contact-role">Managing Partner</p>
      <address class="contact-address">Level 9, 47 Calder Lane<br>Sydney NSW 2000</address>
      <ul class="contact-list">
        <li><svg class="icon" viewBox="0 0 14 14"><path d="M3 1.5 L5 1.5 L6 4.5 L4.5 5.5 Q5.5 8.5 8.5 9.5 L9.5 8 L12.5 9 L12.5 11 Q12 12.5 10.5 12.5 Q2 11 1.5 3.5 Q1.5 2 3 1.5 Z"/></svg>02 7304 6219</li>
        <li><svg class="icon" viewBox="0 0 14 14"><rect x="3.5" y="1" width="7" height="12" rx="1.2"/><line x1="6" y1="11" x2="8" y2="11"/></svg>02 7462 3158</li>
        <li><svg class="icon" viewBox="0 0 14 14"><rect x="1" y="3" width="12" height="8.5"/><path d="M1 3 L7 8 L13 3"/></svg>paul@wbrlegal.com.au</li>
        <li><svg class="icon" viewBox="0 0 14 14"><circle cx="7" cy="7" r="5.8"/><ellipse cx="7" cy="7" rx="2.5" ry="5.8"/><line x1="1.2" y1="7" x2="12.8" y2="7"/></svg>www.wbrlegal.com.au</li>
      </ul>
    </div>
  </section>
</main>
</body>
</html>
```